Slick Quillnest Ad

We've recently re-branded our business to reflect our ethos "Wealth is about more than money - it's about choice." We aim to protect your hard-earned success and help achieve your lifestyle aspirations, whether that's retiring at fifty to go globetrotting, or buying your first home. We're a financial consultancy that primarily services high-net-worth clients.

Our brand is minimalist, modern (check out our website) and the brief focuses on our strong investment return for the past 12 years.

Task: The attached brief is for a Quillnest advertisement. Please see competitor images as a guide to how 'returns' and 'branding' can both be displayed in a design.

Target Market(s)

+30

Font styles to use
Sans Serif

Requirements
Must have
• Creative should feature the strong investment return, and design aesthetic should be 'on-brand' (modern, minimalist, lifestyle focused).

```html
<!DOCTYPE html>
<html lang="en">
<head>
<meta charset="utf-8">
<title>Quillnest – Wealth is about more than money</title>
<link rel="stylesheet" href="https://fonts.googleapis.com/css2?family=Roboto+Condensed:wght@400;700&display=swap">
<style>
  :root {
    --sky-top: #0f3f6b;
    --sky-mid: #3f78a6;
    --horizon: #e0b878;
    --water-top: #6b8fa6;
    --water-deep: #0d2a44;
    --band: rgba(8, 18, 30, 0.78);
    --text-light: #ffffff;
    --device-body: #f4f5f7;
    --device-edge: #d9dce1;
    --device-lens: #2a2d33;
    --brand-green: #b7c42a;
    --screen-top: #8fb6d4;
    --screen-mid: #c9d2d6;
    --screen-low: #b9c6b2;
  }
  * { box-sizing: border-box; margin: 0; padding: 0; }
  html, body { width: 1200px; height: 629px; overflow: hidden; background: var(--water-deep); }
  body { font-family: "Roboto Condensed", "Arial Narrow", sans-serif; }

  .ad {
    position: relative;
    width: 1200px;
    height: 629px;
    overflow: hidden;
  }
  .ad__scenery {
    position: absolute;
    inset: 0;
    background:
      radial-gradient(ellipse 260px 120px at 70px 195px, rgba(255, 214, 140, 0.85), rgba(255, 214, 140, 0) 70%),
      linear-gradient(180deg,
        var(--sky-top) 0%,
        var(--sky-mid) 22%,
        #9fb5bf 33%,
        var(--horizon) 38%,
        #8fa7b1 42%,
        var(--water-top) 50%,
        #2c4c66 70%,
        var(--water-deep) 100%);
  }
  .ad__headline {
    position: absolute;
    left: 112px;
    top: 281px;
    color: var(--text-light);
    font-weight: 400;
    font-size: 31px;
    line-height: 46px;
    letter-spacing: 0.1px;
  }
  .ad__returns {
    position: absolute;
    left: 113px;
    top: 394px;
    display: flex;
    align-items: baseline;
    gap: 10px;
    color: var(--text-light);
    font-size: 20px;
    letter-spacing: 0.3px;
  }
  .ad__returns-figure {
    color: var(--brand-green);
    font-weight: 700;
    font-size: 26px;
  }
  .ad__band {
    position: absolute;
    left: 0;
    right: 0;
    bottom: 0;
    height: 64px;
    background: var(--band);
  }
  .ad__cta {
    position: absolute;
    left: 116px;
    top: 587px;
    display: flex;
    align-items: center;
    gap: 22px;
    color: var(--text-light);
    font-weight: 700;
    font-size: 21px;
    letter-spacing: 0.3px;
    text-decoration: none;
  }
  .ad__cta svg { display: block; }

  .device {
    position: absolute;
    left: 808px;
    top: 28px;
    width: 250px;
    height: 562px;
    border-radius: 42px;
    background: linear-gradient(90deg, var(--device-edge), var(--device-body) 8%, var(--device-body) 92%, var(--device-edge));
    box-shadow: 0 6px 18px rgba(0, 0, 0, 0.35);
  }
  .device__button {
    position: absolute;
    left: -3px;
    width: 4px;
    border-radius: 2px;
    background: var(--device-edge);
  }
  .device__button--one { top: 95px; height: 22px; }
  .device__button--two { top: 128px; height: 34px; }
  .device__lens {
    position: absolute;
    left: 116px;
    top: 32px;
    width: 9px;
    height: 9px;
    border-radius: 50%;
    background: var(--device-lens);
  }
  .device__screen {
    position: absolute;
    left: 5px;
    top: 67px;
    width: 236px;
    height: 436px;
    background: linear-gradient(180deg,
      var(--screen-top) 0%,
      #b6cad7 22%,
      var(--screen-mid) 48%,
      var(--screen-low) 75%,
      #a9b1b3 100%);
  }
  .brand {
    position: absolute;
    left: 0;
    right: 0;
    top: 180px;
    display: flex;
    align-items: center;
    justify-content: center;
    gap: 8px;
    color: var(--brand-green);
    font-weight: 700;
    font-size: 28px;
  }
  .brand__dot {
    width: 14px;
    height: 14px;
    border-radius: 50%;
    background: var(--brand-green);
  }
</style>
</head>
<body>
  <main class="ad">
    <div class="ad__scenery" role="img" aria-label="Aerial photograph of a coastal city skyline at sunrise, with a bridge crossing the bay, marinas and calm blue water"></div>

    <h1 class="ad__headline">Wealth is about more than<br>money - it's about choice</h1>

    <p class="ad__returns">
      <span class="ad__returns-figure">12 years</span>
      <span>of strong investment returns</span>
    </p>

    <div class="ad__band"></div>
    <a class="ad__cta" href="#">
      <span>LEARN MORE</span>
      <svg width="20" height="26" viewBox="0 0 20 26" aria-hidden="true">
        <path d="M4 2 L16 13 L4 24" fill="none" stroke="#ffffff" stroke-width="4.5" stroke-linejoin="miter"/>
      </svg>
    </a>

    <div class="device">
      <span class="device__button device__button--one"></span>
      <span class="device__button device__button--two"></span>
      <span class="device__lens"></span>
      <div class="device__screen" role="img" aria-label="Close view of the city waterfront with towers, a park and an arena">
        <div class="brand"><span class="brand__dot"></span><span>Quillnest</span></div>
      </div>
    </div>
  </main>
</body>
</html>
```